Autobody repair paint repairs spray painting bodywork crash repairs

Details for my new Facebook Design Project will be added sooAUTOMOTIVE REPAIR. CAR / MOTORCYCLES GOT LOGO DESIGN / DID THINK ABOUT FACEBOOK DONT NOALREADY HAVE WEB ADRESS www.brightpanel.co.uk and mail sales@brightpanel,co.uk NEED SOMETHINK I CAN MANAGE TO UPLOAD PICTURES IN TO A GALLERY OR SOMETHINGLIKE THAT I ALSO SELL CAR AND MOTORCYCLES MAYBE A SELLS PAGE WITH A COINDROP LINKn.
Updates

Target Market(s)

general public and trade

Industry/Entity Type

Auto Repair

Font styles to use
Serif
Sans Serif

Colors

Designer to choose colors to be used in the design.

Requirements
Must have
• copy description from my website
• coindrop link. to my site shop
• plenty of logo within reason
Nice to have
• scolling shop
• easy to manage

```html
<!DOCTYPE html>
<html lang="en">
<head>
<meta charset="utf-8">
<title>BrightPanel Bodyshop – Automotive Repair Banner</title>
<link rel="stylesheet" href="https://fonts.googleapis.com/css2?family=Anton&family=Montserrat:wght@700;800;900&family=Oswald:wght@600&family=Open+Sans:wght@400;600;700&display=swap">
<style>
  :root {
    --page: #efefef;
    --night: #0b0b0c;
    --night-soft: #1d1a19;
    --red: #e5242b;
    --red-deep: #a8151b;
    --white: #ffffff;
    --photo-red: #c7262b;
    --photo-grey: #6d6f73;
  }
  html, body { margin: 0; padding: 0; }
  body {
    width: 1200px; height: 1018px; overflow: hidden;
    background: var(--page);
    font-family: "Open Sans", sans-serif;
  }
  .banner {
    position: absolute; left: 0; top: 195px;
    width: 1200px; height: 628px; overflow: hidden;
    background: var(--night);
  }
  .banner__backdrop {
    position: absolute; inset: 0;
    background:
      radial-gradient(ellipse 420px 160px at 560px 250px, rgba(120,60,30,.45), transparent 70%),
      linear-gradient(180deg, #0a0a0b 0%, var(--night-soft) 55%, #121212 100%);
  }
  .banner__swoosh { position: absolute; inset: 0; }
  .headline { position: absolute; left: 0; top: 70px; width: 700px; height: 210px; }
  .headline text {
    font-family: "Anton", sans-serif; fill: var(--red);
    stroke: var(--white); stroke-width: 10px; paint-order: stroke fill;
    text-anchor: middle;
  }
  .services {
    position: absolute; left: 60px; top: 277px; width: 582px;
    margin: 0; text-align: center; color: var(--white);
    font: 700 13.5px/25px "Open Sans", sans-serif; letter-spacing: 3.2px;
  }
  .sales-line {
    position: absolute; left: 58px; top: 356px; margin: 0;
    color: var(--white); font: 800 29px/40px "Montserrat", sans-serif;
  }
  .brand {
    position: absolute; left: 773px; top: 70px; width: 340px;
    text-align: center; color: var(--white);
    font: 800 30px/40px "Montserrat", sans-serif; letter-spacing: 2px;
  }
  .car-photo {
    position: absolute; left: 660px; top: 178px; width: 470px; height: 196px;
    border-radius: 90px 120px 30px 30px;
    background: radial-gradient(ellipse at 55% 45%, #e0262c 0%, var(--photo-red) 55%, #5a0e10 100%);
  }
  .phone { position: absolute; left: 48px; top: 474px; display: flex; align-items: center; gap: 14px; }
  .phone__number { color: var(--white); font: 600 49px/56px "Oswald", sans-serif; letter-spacing: .5px; }
  .divider-dots { position: absolute; left: 409px; top: 484px; }
  .contact-icons { position: absolute; left: 440px; top: 466px; }
  .contact-text {
    position: absolute; left: 489px; color: var(--white);
    font: 400 12.5px/16px "Open Sans", sans-serif; margin: 0;
  }
  .contact-text--address { top: 466px; }
  .contact-text--web { top: 506px; font-size: 11.5px; line-height: 15px; }
  .payment { position: absolute; left: 58px; top: 558px; display: flex; align-items: center; gap: 10px; }
  .payment__label { color: var(--white); font: 400 13px "Open Sans", sans-serif; }
  .payment__link {
    margin-left: 10px; padding: 2px 14px; border-radius: 10px;
    background: var(--white); border: 2px solid #1c3f94;
    font: 600 13.5px/18px "Open Sans", sans-serif; color: #111;
  }
  .gallery { position: absolute; left: 735px; top: 402px; }
  .shop-button {
    position: absolute; left: 852px; top: 561px; width: 152px; height: 32px;
    border-radius: 6px; border: 1.5px solid #ff8a8a;
    background: linear-gradient(180deg, #f0353a, #b3161b);
    color: var(--white); font: 900 17px/31px "Montserrat", sans-serif;
    letter-spacing: 1.5px; text-align: center;
  }
</style>
</head>
<body>
<section class="banner">
  <div class="banner__backdrop" role="img" aria-label="Night road photograph with a starry sky"></div>

  <svg class="banner__swoosh" width="1200" height="628" viewBox="0 0 1200 628" aria-hidden="true">
    <defs>
      <linearGradient id="swoosh-fill" x1="0" x2="1" y1="0" y2="0">
        <stop offset="0" stop-color="#ee2b31"/>
        <stop offset=".6" stop-color="#d71f26"/>
        <stop offset="1" stop-color="#e5242b"/>
      </linearGradient>
    </defs>
    <path d="M0 46 C260 18 560 80 800 175 C900 215 1050 300 1200 318 L1200 408 C1060 402 940 340 810 270 C620 190 300 190 0 305 Z" fill="url(#swoosh-fill)"/>
    <path d="M0 46 C260 18 560 80 800 175 L800 188 C560 100 260 40 0 68 Z" fill="#a8151b" opacity=".8"/>
  </svg>

  <svg class="headline" viewBox="0 0 700 210" aria-label="Automotive Repair">
    <text x="343" y="91" font-size="88" textLength="470" lengthAdjust="spacingAndGlyphs">AUTOMOTIVE</text>
    <text x="372" y="190" font-size="108" textLength="350" lengthAdjust="spacingAndGlyphs">REPAIR</text>
  </svg>

  <p class="services">AUTOMOTIVE BODY REPAIRS | MOTORCYCLE PAINTING<br>WHEELS | BUMPERS | CUSTOM PAINTING</p>
  <p class="sales-line">ALSO SELL CAR AND MOTORCYCLES</p>

  <div class="brand">BRIGHTPANEL BODYSHOP</div>

  <div class="car-photo" role="img" aria-label="Photograph of a red sports car"></div>

  <div class="phone">
    <svg width="52" height="56" viewBox="0 0 52 56" aria-hidden="true">
      <polygon points="26,1 50,14 50,42 26,55 2,42 2,14" fill="var(--red)"/>
      <path d="M18 17 l5 -2 4 8 -3 3 c2 4 5 7 9 9 l3 -3 8 4 -2 5 c-12 1 -26 -13 -24 -24z" fill="#fff"/>
    </svg>
    <span class="phone__number">0770 900 1234</span>
  </div>

  <svg class="divider-dots" width="6" height="50" viewBox="0 0 6 50" aria-hidden="true">
    <g fill="#fff"><circle cx="3" cy="3" r="2.5"/><circle cx="3" cy="14" r="2.5"/><circle cx="3" cy="25" r="2.5"/><circle cx="3" cy="36" r="2.5"/><circle cx="3" cy="47" r="2.5"/></g>
  </svg>

  <svg class="contact-icons" width="32" height="76" viewBox="0 0 32 76" aria-hidden="true">
    <polygon points="16,1 31,9 31,26 16,34 1,26 1,9" fill="var(--red)"/>
    <path d="M16 9 a6 6 0 0 1 6 6 c0 4 -6 11 -6 11 s-6 -7 -6 -11 a6 6 0 0 1 6 -6z" fill="#fff"/>
    <circle cx="16" cy="15" r="2.2" fill="var(--red)"/>
    <polygon points="16,41 31,49 31,66 16,74 1,66 1,49" fill="var(--red)"/>
    <rect x="9" y="52" width="14" height="10" rx="1.5" fill="#fff"/>
    <path d="M9 53 l7 5 7 -5" fill="none" stroke="var(--red)" stroke-width="1.5"/>
  </svg>

  <p class="contact-text contact-text--address">Oakfield Business Park, Brook Lane,<br>Ashford, Kent, TN24 8QR</p>
  <p class="contact-text contact-text--web">sales@brightpanel.co.uk<br>www.brightpanel.co.uk</p>

  <div class="payment">
    <svg width="28" height="28" viewBox="0 0 28 28" aria-hidden="true"><circle cx="14" cy="14" r="12" fill="#1c3f94"/></svg>
    <span class="payment__label">Pay with CoinDrop</span>
    <span class="payment__link">coindrop.me/brightpanel01</span>
  </div>

  <svg class="gallery" width="420" height="150" viewBox="0 0 420 150" aria-label="Workshop photo gallery">
    <g stroke="#fff" stroke-width="6">
      <polygon role="img" aria-label="Photo of a technician repairing a car panel" points="65,4 124,38 124,108 65,142 6,108 6,38" fill="#6b6e72"/>
      <polygon role="img" aria-label="Photo of a red car body in the paint shop" points="200,4 259,38 259,108 200,142 141,108 141,38" fill="var(--photo-red)"/>
      <polygon role="img" aria-label="Photo of a motorcycle in the workshop" points="338,4 397,38 397,108 338,142 279,108 279,38" fill="#3a3b3e"/>
    </g>
  </svg>

  <div class="shop-button">SHOP NOW</div>
</section>
</body>
</html>
```